Online shopping portal - Business Card Design

Brivanto.com.au is a complete shopping experience. Search, compare & buy items from partnered stores & receive cashbash for your purchases and referrals.
Mission
Our mission is to provide a system for entrepreneurs to create an ongoing income, while providing consumers worldwide with a better way to shop.
A product brokerage and Internet marketing company that specialises in One-to-One Marketing, Quelden Australia is a subsidiary of Quelden Norvik Worldwide, Inc.
With more than 3 million Preferred Customers and 180,000 Customer Managers worldwide, Quelden Norvik has generated over $3 billion USD in accumulated retail sales. The Company employs more than 675 people globally with international operations in Australia, United States, Canada, Taiwan, Hong Kong, Mexico & Singapore
Through revolutionary technology and the one-to-one marketing and social shopping Quelden Australia are leveraging the Internet with the power of people to create the economy of the future.
By providing online shoppers with the products and services they want and need — backed by the Company’s people power — Quelden Australia is fast becoming the World Wide Web’s ultimate online shopping destination.
As a result, we are changing the way people shop and changing the economic paradigm where anyone can become financially independent by creating their own economy — Rooted in Goods. Lifted by Folk®.
Description
Welcome to a new kind of comparison shopping site where you get PAID cashback to shop!
Simply create an account to start accumulating cash backs each time you make purchases across hundreds of trusted Partner Stores and thousands of your favorite brands through our convenient SwiftTote® for one stop shopping.
All merchant stores are backed by PELMARO.COM's 100% satisfaction guarantee.

Updates
Project Deadline Extended
Reason: Hi all,  I am extending the deadline as i'm going to be away for my birthday (and may not have time to check before the current deadline anyway)  I figure that the more time i give you the better.

Industry/Entity Type
Online Shopping
Contact Information for Business Card
Business Name: Brivanto.com.au
website: www.brivanto.com.au
Facebook: www.facebook.com/brivanto.com.au.
Email: info@brivanto.com.au
Phone: Mirel on 0497 28 14 56
Requirements
Nice to have
- Create a Brivanto logo

```html
<!DOCTYPE html>
<html lang="en">
<head>
<meta charset="utf-8">
<title>Brivanto Business Card</title>
<link href="https://fonts.googleapis.com/css2?family=Exo+2:wght@400;500;800&display=swap" rel="stylesheet">
<style>
  :root {
    --bg: #e6e8ea;
    --card: #ffffff;
    --brand: #1f63b0;
    --ink: #10304f;
    --ink-soft: #1d4468;
    --cyan-light: #22e0f0;
    --cyan-mid: #15aee0;
    --blue-deep: #1a6fc4;
  }
  * { box-sizing: border-box; margin: 0; padding: 0; }
  html, body { width: 1200px; height: 901px; overflow: hidden; }
  body {
    background: var(--bg);
    font-family: "Exo 2", sans-serif;
    position: relative;
  }
  .card {
    position: absolute;
    width: 520px;
    height: 300px;
    border-radius: 30px;
    background: var(--card);
    overflow: hidden;
    box-shadow: 0 10px 26px rgba(0,0,0,0.18);
  }
  .card--back { left: 50px; top: 300px; }
  .card--front { left: 630px; top: 300px; }

  .card__wave { position: absolute; inset: 0; width: 100%; height: 100%; }

  .wordmark {
    position: absolute;
    display: flex;
    align-items: center;
    gap: 8px;
    font-family: "Exo 2", sans-serif;
    font-weight: 800;
    color: var(--brand);
    letter-spacing: 1px;
    text-transform: uppercase;
    line-height: 1;
  }
  .wordmark__dot {
    width: 12px; height: 12px;
    background: var(--ink);
  }
  .card--back .wordmark { left: 150px; top: 40px; font-size: 40px; }
  .card--front .wordmark { left: 88px; top: 118px; font-size: 58px; }
  .card--front .wordmark__dot { width: 16px; height: 16px; }

  .contact {
    position: absolute;
    right: 34px;
    bottom: 22px;
    text-align: right;
    color: var(--ink);
  }
  .contact__name {
    font-size: 17px;
    font-weight: 500;
    letter-spacing: 1.5px;
    text-transform: uppercase;
    line-height: 1.2;
  }
  .contact__role {
    font-size: 13px;
    line-height: 1.2;
    color: var(--ink-soft);
    margin-bottom: 7px;
  }
  .contact__address {
    font-size: 12px;
    line-height: 1.35;
    margin-bottom: 6px;
  }
  .contact__list { list-style: none; }
  .contact__item {
    display: flex;
    justify-content: flex-end;
    align-items: center;
    gap: 7px;
    font-size: 12px;
    line-height: 1.5;
  }
  .contact__icon { width: 11px; height: 11px; fill: var(--ink); flex: none; }
</style>
</head>
<body>

<section class="card card--back" aria-label="Business card, contact side">
  <svg class="card__wave" viewBox="0 0 520 300" preserveAspectRatio="none" aria-hidden="true">
    <defs>
      <radialGradient id="waveGlow" cx="0.45" cy="0.55" r="0.8">
        <stop offset="0" stop-color="#22e0f0"/>
        <stop offset="0.5" stop-color="#15aee0"/>
        <stop offset="1" stop-color="#1a6fc4"/>
      </radialGradient>
    </defs>
    <path d="M0 70 C 60 150, 200 150, 300 120 C 380 98, 450 80, 520 84 L520 300 L0 300 Z" fill="url(#waveGlow)"/>
    <path d="M0 70 C 60 150, 200 150, 300 120 C 380 98, 450 80, 520 84" fill="none" stroke="#ffffff" stroke-opacity="0.35" stroke-width="3"/>
  </svg>

  <div class="wordmark"><span>Brivanto</span><span class="wordmark__dot"></span></div>

  <div class="contact">
    <p class="contact__name">Daniel Corwen</p>
    <p class="contact__role">Managing Director</p>
    <p class="contact__address">06 2 14th floor Plaza<br>Harrow Road BNV</p>
    <ul class="contact__list">
      <li class="contact__item">0497 28 14 56
        <svg class="contact__icon" viewBox="0 0 12 12" aria-hidden="true"><path d="M2.5 1 L4.5 1 L5 3.5 L3.8 4.3 C4.4 5.8 5.7 7.1 7.4 7.9 L8.2 6.8 L11 7.4 L11 9.5 C11 10.3 10.3 11 9.5 11 C5 11 1 7 1 2.5 C1 1.7 1.7 1 2.5 1 Z"/></svg>
      </li>
      <li class="contact__item">0497 28 14 57
        <svg class="contact__icon" viewBox="0 0 12 12" aria-hidden="true"><path d="M3 0.5 H9 A1 1 0 0 1 10 1.5 V10.5 A1 1 0 0 1 9 11.5 H3 A1 1 0 0 1 2 10.5 V1.5 A1 1 0 0 1 3 0.5 Z M3.2 2 V9 H8.8 V2 Z" fill-rule="evenodd"/></svg>
      </li>
      <li class="contact__item">info@brivanto.com.au
        <svg class="contact__icon" viewBox="0 0 12 12" aria-hidden="true"><path d="M1 2.5 H11 V9.5 H1 Z M1.6 3 L6 6.5 L10.4 3 Z" fill-rule="evenodd"/></svg>
      </li>
      <li class="contact__item">www.brivanto.com.au
        <svg class="contact__icon" viewBox="0 0 12 12" aria-hidden="true"><circle cx="6" cy="6" r="5" fill="none" stroke="#10304f" stroke-width="1.2"/><path d="M1 6 H11 M6 1 C3.5 3.5 3.5 8.5 6 11 M6 1 C8.5 3.5 8.5 8.5 6 11" fill="none" stroke="#10304f" stroke-width="0.9"/></svg>
      </li>
    </ul>
  </div>
</section>

<section class="card card--front" aria-label="Business card, brand side">
  <div class="wordmark"><span>Brivanto</span><span class="wordmark__dot"></span></div>
</section>

</body>
</html>
```